Fitness Tracker for Fitness Club

We need a graphic design for a fitness app.

The app will display videos of live workouts, provide the ability to communicate to a trainer through an inbox, and the ability to track weight over time.

The layout provided is the current demo mobile html application, we would like to change this to a custom app and would like a new design, something that is clean and current. Something like kinora feel. User should feel like the app is clean and cutting edge.

The current demo is to display functionality only, we are hoping for a complete redesign of the app.

```html
<!DOCTYPE html>
<html lang="en">
<head>
<meta charset="utf-8">
<title>Solvar Fitness – App Screens</title>
<link href="https://fonts.googleapis.com/css2?family=Open+Sans:wght@400;600;700&family=Roboto:wght@400;500&display=swap" rel="stylesheet">
<style>
  :root {
    --stage: #0d0d0d;
    --brand-grey: #9c9c9c;
    --splash-top: #6e625a;
    --splash-bottom: #3d3a3c;
    --login-top: #8fa696;
    --login-mid: #4b5462;
    --login-bottom: #03031e;
    --field: #ffffff;
    --field-text: #a8a8a8;
    --accent-teal: #36b6c4;
    --button: #5b5e72;
    --button-border: #d6d6d6;
    --header: #8b8b8b;
    --header-text: #ececec;
    --menu: #3a3a3a;
    --menu-divider: #555555;
    --menu-accent: #e0222f;
    --icon-bg: #5a5a5a;
    --white: #ffffff;
  }
  * { box-sizing: border-box; margin: 0; padding: 0; }
  html, body {
    width: 1200px; height: 732px; overflow: hidden;
    background: var(--stage);
  }
  .stage { position: relative; width: 1200px; height: 732px; }
  .screen {
    position: absolute; top: 113px; width: 274px; height: 487px; overflow: hidden;
  }

  /* Splash */
  .screen--splash { left: 77px; }
  .splash-photo {
    position: absolute; inset: 0;
    background: linear-gradient(160deg, var(--splash-top) 0%, #8a7c70 45%, var(--splash-bottom) 100%);
  }
  .splash-badge {
    position: absolute; left: 62px; top: 119px; width: 150px; height: 150px;
    border-radius: 50%; background: #0a0a0a; border: 4px solid #5a5a5a;
    display: flex; align-items: center; justify-content: center; text-align: center;
  }
  .brand-name {
    font-family: "Open Sans", sans-serif; font-weight: 700; color: var(--brand-grey);
    line-height: 1.1;
  }
  .splash-badge .brand-name { font-size: 20px; }
  .brand-city { display: block; font-size: 9px; margin-top: 4px; }

  /* Sign in */
  .screen--login {
    left: 468px;
    background: linear-gradient(180deg, var(--login-top) 0%, var(--login-mid) 55%, var(--login-bottom) 100%);
    font-family: "Open Sans", sans-serif;
  }
  .login-title {
    position: absolute; top: 22px; width: 100%; text-align: center;
    color: var(--white); font-size: 18px; font-weight: 700;
  }
  .login-badge {
    position: absolute; left: 89px; top: 69px; width: 94px; height: 94px;
    border-radius: 50%; background: var(--white); border: 5px solid #b9c2bb;
    display: flex; align-items: center; justify-content: center; text-align: center;
  }
  .login-badge .brand-name { font-size: 13px; color: #4a4a4a; }
  .login-badge .brand-city { font-size: 6px; margin-top: 2px; }
  .field {
    position: absolute; left: 17px; width: 238px; height: 30px;
    background: var(--field); display: flex; align-items: center; justify-content: space-between;
    padding: 0 8px; font-size: 11px; color: var(--field-text);
  }
  .field--username { top: 182px; }
  .field--password { top: 226px; }
  .remember {
    position: absolute; left: 17px; top: 268px; display: flex; align-items: center; gap: 6px;
    color: #e6e6e6; font-size: 10px;
  }
  .btn-signin {
    position: absolute; left: 63px; top: 337px; width: 144px; height: 31px;
    background: var(--button); border: 1px solid var(--button-border);
    color: var(--white); font-size: 12px; display: flex; align-items: center; justify-content: center;
  }
  .forgot {
    position: absolute; top: 378px; width: 100%; text-align: center; color: #e0e0e0; font-size: 10px;
  }

  /* Tracker home */
  .screen--home { left: 860px; background: var(--menu); font-family: "Roboto", sans-serif; }
  .app-header {
    position: absolute; top: 0; left: 0; width: 100%; height: 56px; background: var(--header);
  }
  .menu-button { position: absolute; left: 7px; top: 11px; }
  .app-title {
    position: absolute; width: 100%; top: 19px; text-align: center; padding-left: 0;
    color: var(--header-text); font-size: 14px;
  }
  .video-still {
    position: absolute; top: 56px; left: 0; width: 100%; height: 251px;
    background: linear-gradient(170deg, #d9c6ae 0%, #b79a7e 40%, #6c7fae 75%, #c8b8a8 100%);
  }
  .play-button { position: absolute; left: 93px; top: 69px; }
  .menu-list { position: absolute; top: 307px; left: 0; width: 100%; list-style: none; }
  .menu-item {
    height: 44px; display: flex; align-items: center; justify-content: space-between;
    padding: 0 6px 0 12px; color: var(--white); font-size: 18px;
    border-left: 4px solid var(--menu-accent); border-bottom: 1px solid var(--menu-divider);
  }
  .menu-icon {
    width: 32px; height: 32px; border-radius: 50%; background: var(--icon-bg);
    display: flex; align-items: center; justify-content: center;
  }
</style>
</head>
<body>
<main class="stage">

  <section class="screen screen--splash">
    <div class="splash-photo" role="img" aria-label="Photo of a woman lifting dumbbells in a gym, warm and dimmed"></div>
    <div class="splash-badge">
      <span class="brand-name">Solvar Fitness<span class="brand-city">Ridgeport</span></span>
    </div>
  </section>

  <section class="screen screen--login">
    <h1 class="login-title">Sign In</h1>
    <div class="login-badge">
      <span class="brand-name">Solvar Fitness<span class="brand-city">Ridgeport</span></span>
    </div>
    <div class="field field--username">Username
      <svg width="12" height="12" viewBox="0 0 12 12"><rect x="1" y="1" width="10" height="10" fill="none" stroke="var(--accent-teal)" stroke-width="1.3"/><path d="M3 6l2 2 4-4" fill="none" stroke="var(--accent-teal)" stroke-width="1.4"/></svg>
    </div>
    <div class="field field--password">Password
      <svg width="12" height="12" viewBox="0 0 12 12"><rect x="1" y="1" width="10" height="10" fill="none" stroke="var(--accent-teal)" stroke-width="1.3"/><path d="M3 6l2 2 4-4" fill="none" stroke="var(--accent-teal)" stroke-width="1.4"/></svg>
    </div>
    <div class="remember">
      <svg width="11" height="11" viewBox="0 0 12 12"><rect x="1" y="1" width="10" height="10" fill="none" stroke="#e6e6e6" stroke-width="1.3"/><path d="M3 6l2 2 4-4" fill="none" stroke="#e6e6e6" stroke-width="1.4"/></svg>
      Keep me logged in
    </div>
    <div class="btn-signin">Sign in</div>
    <div class="forgot">Forgot password</div>
  </section>

  <section class="screen screen--home">
    <header class="app-header">
      <svg class="menu-button" width="37" height="37" viewBox="0 0 37 37">
        <rect width="37" height="37" fill="var(--white)"/>
        <rect x="5" y="5" width="27" height="6" fill="var(--menu)"/>
        <rect x="5" y="15.5" width="27" height="6" fill="var(--menu)"/>
        <rect x="5" y="26" width="27" height="6" fill="var(--menu)"/>
      </svg>
      <div class="app-title">Fitness Tracker</div>
    </header>
    <div class="video-still" role="img" aria-label="Workout video still: group class doing dumbbell presses on exercise balls">
      <svg class="play-button" width="80" height="80" viewBox="0 0 80 80">
        <circle cx="40" cy="40" r="40" fill="rgba(40,40,40,0.65)"/>
        <path d="M31 24 L57 40 L31 56 Z" fill="var(--white)"/>
      </svg>
    </div>
    <ul class="menu-list">
      <li class="menu-item">Available sessions
        <span class="menu-icon"><svg width="18" height="14" viewBox="0 0 18 14"><rect x="1" y="5" width="11" height="8" fill="#fff"/><circle cx="4" cy="3" r="2.5" fill="#fff"/><circle cx="9" cy="3" r="2.5" fill="#fff"/><path d="M12 8l5-3v8l-5-3z" fill="#fff"/></svg></span>
      </li>
      <li class="menu-item">Weight Accountability
        <span class="menu-icon"><svg width="18" height="18" viewBox="0 0 18 18"><circle cx="9" cy="9" r="7" fill="none" stroke="#fff" stroke-width="2"/><path d="M9 5v4l3 2" fill="none" stroke="#fff" stroke-width="2"/></svg></span>
      </li>
      <li class="menu-item">Inbox (3)
        <span class="menu-icon"><svg width="18" height="13" viewBox="0 0 18 13"><rect x="1" y="1" width="16" height="11" fill="#fff"/><path d="M1 1l8 6 8-6" fill="none" stroke="var(--icon-bg)" stroke-width="1.5"/></svg></span>
      </li>
      <li class="menu-item">Profile
        <span class="menu-icon"><svg width="20" height="14" viewBox="0 0 20 14"><rect x="1" y="1" width="18" height="12" fill="none" stroke="#fff" stroke-width="1.6"/><rect x="3.5" y="4" width="5" height="6" fill="#fff"/><path d="M11 5h6M11 8h6M11 11h4" stroke="#fff" stroke-width="1.3"/></svg></span>
      </li>
    </ul>
  </section>

</main>
</body>
</html>
```